Website Required for Small Cyber Security Company

Require a website for Cyber Security company. I have logo which i will attach. Please use logo blue and white as a guide
Would ultimately like the site to have a technology theme with the following pages Landing page
Services
Contact
Careers

I can provide content for each of those pages in due course, until then happy for you to use dummy data to display purposes

Target Market(s)

Government

Industry/Entity Type

Cyber Security

Coding

Coded - Design and coding required

Number of Pages Required

4 page

Colors
0054AA
0677BA
7BADD7
CADEEF
E8F1F8

Requirements
Must have
• High quality finish and UX
Nice to have
• look and feel professional and not cheap

```html
<!DOCTYPE html>
<html lang="en">
<head>
<meta charset="utf-8">
<title>Harrow Bay Consulting – Cyber Security</title>
<link href="https://fonts.googleapis.com/css2?family=Open+Sans:wght@400;600;700&family=Ubuntu:wght@400;500;700&display=swap" rel="stylesheet">
<style>
:root{
  --navy:#1c3a5f;
  --navy-deep:#162e4d;
  --navy-band:#233f66;
  --blue:#0054AA;
  --blue-mid:#0677BA;
  --sky:#7BADD7;
  --pale:#CADEEF;
  --ice:#E8F1F8;
  --teal:#00a7d8;
  --accent:#1a9ed8;
  --gray-bg:#f4f5f7;
  --text:#8a8f98;
  --heading:#1f3a5c;
  --white:#ffffff;
}
*{box-sizing:border-box;margin:0;padding:0}
html,body{width:1200px;height:5017px;overflow:hidden}
body{position:relative;font-family:"Open Sans",sans-serif;color:var(--text);background:var(--white)}
.abs{position:absolute}
section,header{position:absolute;left:0;width:1200px;overflow:hidden}
h1,h2,h3{font-family:"Ubuntu",sans-serif;font-weight:500}
.label{font-size:10px;font-weight:700;letter-spacing:.5px;text-transform:uppercase}
.center{text-align:center;left:0;width:1200px}
.rule{height:3px;width:60px;background:var(--teal)}
.btn{display:flex;align-items:center;justify-content:center;gap:14px;color:var(--white);font-weight:700;font-size:15px}

/* top bar */
.topbar{top:0;height:28px;background:var(--navy-band);color:var(--white);font-size:11px;display:flex;justify-content:center;align-items:center;gap:46px}
.topbar b{font-weight:700}
.topbar span{display:flex;align-items:center;gap:6px}

/* nav */
.nav{top:28px;height:81px;background:var(--white)}
.brand{left:88px;top:22px;display:flex;align-items:center;gap:8px;font-family:"Ubuntu",sans-serif;font-weight:700;font-size:14px;color:var(--navy)}
.brand i{width:22px;height:22px;border-radius:50%;border:2px solid var(--blue)}
.menu a{position:absolute;top:36px;font-size:14px;font-weight:600;color:#6b7480;text-decoration:none}
.menu a.active{color:var(--blue);font-weight:700}

/* hero */
.hero{top:109px;height:672px;background:linear-gradient(100deg,#2a3d58 0%,#3a4c63 45%,#4c5a6b 70%,#2f3f55 100%)}
.hero .overlay{inset:0;background:linear-gradient(90deg,rgba(22,42,72,.75),rgba(22,42,72,.35))}
.hero .tag{left:95px;top:218px;color:#d6dde8;font-size:12px;display:flex;align-items:center;gap:22px}
.hero .tag i{width:44px;height:1px;background:#c9d2de}
.hero h1{left:95px;top:262px;color:var(--white);font-size:42px;line-height:58px;font-weight:700}
.hero p{left:95px;top:404px;color:#e2e7ee;font-size:13px;line-height:22px;width:420px}
.hero .btn{left:95px;top:489px;width:193px;height:39px;background:#2f9fe0;font-size:12px}

/* about */
.about{top:781px;height:695px}
.diamond{left:74px;top:92px;width:506px;height:506px}
.about .txt{left:614px}
.feature{display:flex;align-items:center;gap:14px;font-family:"Ubuntu",sans-serif;font-weight:500;color:var(--heading);font-size:16px;line-height:26px}
.about .para{top:281px;width:494px;font-size:13px;line-height:23.5px}

/* services */
.services{top:1476px;height:661px;background:var(--gray-bg)}
.svc{top:269px;width:320px;height:244px}
.svc .photo{width:320px;height:217px}
.svc .cap{position:absolute;left:26px;top:189px;width:269px;height:55px;background:var(--white);box-shadow:0 4px 10px rgba(0,0,0,.12);display:flex;align-items:center;font-size:14px;color:#4b5563}
.svc .cap i{width:55px;height:55px;background:var(--teal);display:flex;align-items:center;justify-content:center;margin-right:32px}

/* why */
.why{top:2137px;height:541px;background:linear-gradient(110deg,#1f3c6c,#284a7a 50%,#1e3a68)}
.why .col{top:0;width:340px;height:541px;text-align:center;color:var(--white)}
.why .circle{position:absolute;left:131px;top:239px;width:78px;height:78px;border-radius:50%;background:var(--white);display:flex;align-items:center;justify-content:center}
.why h3{position:absolute;left:0;top:344px;width:340px;font-family:"Open Sans",sans-serif;font-weight:700;font-size:17px}
.why p{position:absolute;top:388px;left:20px;width:300px;font-size:13px;line-height:22px;color:#e4e9f1}
.why .more{position:absolute;left:0;top:450px;width:340px;font-size:11px;font-weight:700;display:flex;justify-content:center;gap:10px;align-items:center}

/* done right */
.done{top:2678px;height:606px}
.done .txt{left:647px}

/* reviews */
.reviews{top:3284px;height:676px;background:linear-gradient(110deg,#1d3a66,#26487a 50%,#1c3865)}
.card{top:316px;width:494px;height:238px;background:var(--white);box-shadow:0 6px 0 #c3ccd8;text-align:center}
.card .avatar{position:absolute;left:204px;top:-45px;width:86px;height:86px;border-radius:50%;border:3px solid var(--white)}
.card .q{position:absolute;left:34px;top:36px;font-family:"Ubuntu",sans-serif;font-size:80px;line-height:80px;color:#eef1f5;font-weight:700}
.card p{position:absolute;left:70px;top:66px;width:354px;font-size:15px;line-height:25px;color:#3c4350}
.card .name{position:absolute;left:0;top:154px;width:494px;font-size:15px;font-weight:700;color:var(--heading);text-align:center}
.card .place{position:absolute;left:0;top:181px;width:494px;font-size:11px;color:var(--accent);text-align:center;display:flex;justify-content:center;align-items:center;gap:4px}

/* contact */
.contact{top:3960px;height:1057px}
.form-card{left:164px;top:316px;width:874px;height:457px;background:var(--white);box-shadow:0 0 24px rgba(0,0,0,.08)}
.form-card .bar{left:36px;top:0;width:797px;height:4px;background:#5a6b80}
.form-card h2{left:50px;top:46px;font-size:28px;line-height:35px;color:var(--accent);font-weight:500}
.field{left:50px;width:347px;background:var(--ice);font-size:11px;color:#9aa8b8;padding:10px 15px}
.submit{left:50px;top:335px;width:189px;height:47px;background:var(--navy);color:var(--white);font-weight:700;font-size:15px;display:flex;align-items:center;justify-content:center}
.divider{left:456px;top:20px;width:1px;height:400px;background:#e6e9ee}
.info{left:498px;display:flex;gap:14px;font-size:12px;line-height:25px;color:var(--accent)}
.info i{width:22px;height:22px;border-radius:50%;background:var(--navy);display:flex;align-items:center;justify-content:center;flex:none;margin-top:2px}

/* footer */
.footer-top{left:144px;top:4790px;color:var(--white);font-family:"Ubuntu",sans-serif;font-weight:700;font-size:17px;display:flex;align-items:center;gap:10px}
.footer-top i{width:30px;height:30px;border-radius:50%;border:3px solid var(--white)}
.fitem{top:4796px;color:var(--white);font-size:12px;line-height:18px;display:flex;gap:12px;align-items:center}
.fsep{top:4788px;width:1px;height:44px;background:rgba(255,255,255,.3)}
.fnav{top:4874px;left:253px;width:711px;height:58px;border-top:1px solid rgba(255,255,255,.35);border-bottom:1px solid rgba(255,255,255,.35)}
.fnav a{position:absolute;top:20px;color:var(--white);font-size:13px;text-decoration:none}
.copy{left:148px;top:4974px;color:#cfd7e2;font-size:11px}
.social{top:4970px;width:22px;height:22px;border:1px solid rgba(255,255,255,.7)}
</style>
</head>
<body>

<header class="topbar">
  <span><svg width="11" height="11" viewBox="0 0 12 12"><circle cx="6" cy="6" r="5" fill="none" stroke="#fff"/><path d="M6 3v3l2 1" stroke="#fff" fill="none"/></svg><b>Open hours:</b> Mo-Fr from 9.00-13.00 &amp; 14.00-18.00</span>
  <span><svg width="11" height="11" viewBox="0 0 12 12"><circle cx="6" cy="6" r="5" fill="none" stroke="#fff"/></svg><b>Telephone:</b> 01632 960 418</span>
  <span><svg width="12" height="9" viewBox="0 0 12 9"><rect x=".5" y=".5" width="11" height="8" fill="none" stroke="#fff"/><path d="M.5.5 6 5l5.5-4.5" fill="none" stroke="#fff"/></svg><b>Email:</b> info@harrowbay-mail.net</span>
</header>

<header class="nav">
  <div class="abs brand"><i></i>HARROW BAY</div>
  <nav class="menu">
    <a class="active" style="left:345px">HOME</a>
    <a style="left:448px">SERVICES</a>
    <a style="left:575px">ABOUT US</a>
    <a style="left:725px">BLOG</a>
    <a style="left:843px">CONTACT US</a>
  </nav>
</header>

<section class="hero">
  <div class="abs overlay" role="img" aria-label="Business team meeting around a conference table"></div>
  <div class="abs tag">CyberSecurity <i></i></div>
  <h1 class="abs">Unlocking the Power of<br>Cyber Protection</h1>
  <p class="abs">Lorem ipsum dolor sit amet, consectetur adipiscing elit, sed do eiusmod tempor incididunt ut labore et dolore magna</p>
  <div class="abs btn">Discover more</div>
</section>

<section class="about">
  <svg class="abs diamond" viewBox="0 0 506 506" role="img" aria-label="Collage of four team photos arranged in a diamond">
    <defs>
      <linearGradient id="g1" x1="0" y1="0" x2="1" y2="1"><stop offset="0" stop-color="#c7ccd3"/><stop offset="1" stop-color="#5d6470"/></linearGradient>
      <linearGradient id="g2" x1="0" y1="0" x2="1" y2="1"><stop offset="0" stop-color="#6a84a8"/><stop offset="1" stop-color="#1f3558"/></linearGradient>
      <linearGradient id="g3" x1="0" y1="0" x2="1" y2="1"><stop offset="0" stop-color="#b7b4ae"/><stop offset="1" stop-color="#4a4f58"/></linearGradient>
      <linearGradient id="g4" x1="0" y1="0" x2="1" y2="1"><stop offset="0" stop-color="#d8b89a"/><stop offset="1" stop-color="#6d5a48"/></linearGradient>
    </defs>
    <polygon points="253,8 371,126 253,244 135,126" fill="url(#g1)"/>
    <polygon points="380,135 498,253 380,371 262,253" fill="url(#g2)"/>
    <polygon points="126,135 244,253 126,371 8,253" fill="url(#g3)"/>
    <polygon points="253,262 371,380 253,498 135,380" fill="url(#g4)"/>
    <circle cx="253" cy="253" r="64" fill="#fff"/>
    <circle cx="253" cy="253" r="40" fill="none" stroke="#0054AA" stroke-width="5"/>
  </svg>
  <div class="abs txt label" style="top:110px;color:#6b7480">About our company</div>
  <h2 class="abs txt" style="top:136px;font-size:36px;color:var(--heading)">Your Cybersecurity Partner</h2>
  <div class="abs txt" style="top:228px;font-size:20px;color:var(--accent);font-family:Ubuntu,sans-serif">Elevating Cybersecurity Excellence</div>
  <p class="abs txt para">Lorem ipsum dolor sit amet, consectetur adipiscing elit, sed do eiusmod tempor incididunt ut laborefg et dolore magna aliqua. Ut enim ad minim veniam, quis nostrud exercitation ullamco laboris nisi ut aliquip ex ea commodo consequat. Duis aute irure dolor in reprehenderit in voluptate velit esse cillum dolore eu fugiat nulla pariatur. Excepteur sint occaecat cupidatat non proident, sunt in culpa qui officia deserunt mollit anim id est laborum.</p>
  <div class="abs feature" style="left:617px;top:478px">
    <svg width="52" height="52" viewBox="0 0 52 52"><circle cx="26" cy="26" r="18" fill="none" stroke="#1f3a5c" stroke-width="2"/><circle cx="26" cy="26" r="7" fill="none" stroke="#1f3a5c" stroke-width="2"/><path d="M26 2v14M26 36v14M2 26h14M36 26h14" stroke="#1f3a5c" stroke-width="2"/></svg>
    <span>Client-Centric<br>Approach</span>
  </div>
  <div class="abs feature" style="left:910px;top:478px">
    <svg width="40" height="52" viewBox="0 0 40 52"><path d="M20 10l5 10 11 2-8 8 2 11-10-5-10 5 2-11-8-8 11-2z" fill="none" stroke="#1f3a5c" stroke-width="2"/></svg>
    <span>Proven Track<br>Record</span>
  </div>
  <div class="abs btn" style="left:614px;top:563px;width:156px;height:43px;background:var(--teal)">Contact us
    <svg width="18" height="14" viewBox="0 0 18 14"><path d="M1 7h15M10 1l6 6-6 6" stroke="#fff" stroke-width="2" fill="none"/></svg></div>
</section>

<section class="services">
  <div class="abs center label" style="top:69px">Our services</div>
  <h2 class="abs center" style="top:104px;font-size:36px;color:var(--heading)">Services We Provide</h2>
  <div class="abs rule" style="left:570px;top:153px"></div>
  <p class="abs" style="left:250px;top:183px;width:700px;text-align:center;font-size:13px;line-height:24px">Lorem ipsum dolor sit amet, consectetur adipiscing elit, sed do eiusmod tempor incididunt ut labore fg et dolore magna aliqua. Ut enim ad mi</p>

  <div class="abs svc" style="left:95px">
    <div class="photo" role="img" aria-label="Two analysts working at computer monitors" style="background:linear-gradient(135deg,#5c7896,#243850)"></div>
    <div class="cap"><i><svg width="24" height="24" viewBox="0 0 24 24"><path d="M12 3l8 3v6c0 5-4 8-8 9-4-1-8-4-8-9V6z" fill="none" stroke="#fff" stroke-width="2"/></svg></i>Incidennt Response</div>
  </div>
  <div class="abs svc" style="left:442px">
    <div class="photo" role="img" aria-label="Professional woman holding a tablet in an office" style="background:linear-gradient(135deg,#d7d9dc,#6f747a)"></div>
    <div class="cap"><i><svg width="24" height="24" viewBox="0 0 24 24"><circle cx="12" cy="12" r="9" fill="none" stroke="#fff" stroke-width="2"/><circle cx="12" cy="12" r="4" fill="none" stroke="#fff" stroke-width="2"/></svg></i>Cloud Security</div>
  </div>
  <div class="abs svc" style="left:789px">
    <div class="photo" role="img" aria-label="Two colleagues reviewing work on a laptop" style="background:linear-gradient(135deg,#a8a396,#3b4048)"></div>
    <div class="cap"><i><svg width="24" height="24" viewBox="0 0 24 24"><path d="M4 20h16M8 16l8-10M8 16l-2-6" fill="none" stroke="#fff" stroke-width="2"/></svg></i>Phishing Simulations</div>
  </div>
</section>

<section class="why" role="img" aria-label="Dark blue photo of a team at work behind the content">
  <div class="abs center label" style="top:86px;color:#fff">About our company</div>
  <h2 class="abs center" style="top:120px;font-size:36px;color:#fff">Why Choose Us</h2>
  <div class="abs rule" style="left:570px;top:171px"></div>

  <div class="abs col" style="left:83px">
    <div class="circle"><svg width="30" height="30" viewBox="0 0 30 30"><circle cx="11" cy="11" r="4" fill="none" stroke="#1f3a5c" stroke-width="2"/><circle cx="20" cy="11" r="4" fill="none" stroke="#1f3a5c" stroke-width="2"/><path d="M4 24c0-5 14-5 14 0M14 22c1-4 12-4 12 2" fill="none" stroke="#1f3a5c" stroke-width="2"/></svg></div>
    <h3>Regulatory Compliance</h3>
    <p>Lorem ipsum dolor sit amet, consectetur a dipiscing elit, sed do eiusmod</p>
    <div class="more">APPOINTMENT <svg width="22" height="10" viewBox="0 0 22 10"><path d="M0 5h20M15 1l5 4-5 4" stroke="#fff" fill="none" stroke-width="1.5"/></svg></div>
  </div>
  <div class="abs col" style="left:434px">
    <div class="circle"><svg width="30" height="30" viewBox="0 0 30 30"><path d="M6 20v-5a9 9 0 0118 0v5" fill="none" stroke="#1f3a5c" stroke-width="2"/><rect x="5" y="18" width="5" height="7" fill="#1f3a5c"/><rect x="20" y="18" width="5" height="7" fill="#1f3a5c"/></svg></div>
    <h3>Quality Assurance</h3>
    <p>Lorem ipsum dolor sit amet, consectetur a dipiscing elit, sed do eiusmod</p>
    <div class="more">APPOINTMENT <svg width="22" height="10" viewBox="0 0 22 10"><path d="M0 5h20M15 1l5 4-5 4" stroke="#fff" fill="none" stroke-width="1.5"/></svg></div>
  </div>
  <div class="abs col" style="left:777px">
    <div class="circle"><svg width="30" height="30" viewBox="0 0 30 30"><path d="M15 4l3.5 7 7.5 1-5.5 5.5 1.5 8-7-4-7 4 1.5-8L4 12l7.5-1z" fill="none" stroke="#1f3a5c" stroke-width="2"/></svg></div>
    <h3>Timely Response</h3>
    <p>Lorem ipsum dolor sit amet, consectetur a dipiscing elit, sed do eiusmod</p>
    <div class="more">APPOINTMENT <svg width="22" height="10" viewBox="0 0 22 10"><path d="M0 5h20M15 1l5 4-5 4" stroke="#fff" fill="none" stroke-width="1.5"/></svg></div>
  </div>
</section>

<section class="done">
  <div class="abs" role="img" aria-label="Two businessmen discussing a document on a tablet" style="left:90px;top:147px;width:524px;height:345px;background:linear-gradient(120deg,#c2ccd6,#5a6a80 60%,#2d3b50)"></div>
  <div class="abs txt label" style="top:112px;color:#6b7480">About our company</div>
  <h2 class="abs txt" style="top:135px;font-size:36px;color:var(--heading)">Cybersecurity Done Right</h2>
  <div class="abs txt rule" style="top:195px;width:84px"></div>
  <div class="abs txt" style="top:237px;font-size:20px;color:var(--heading);font-family:Ubuntu,sans-serif">Elevating Your Data's Protection</div>
  <p class="abs txt" style="top:288px;width:495px;font-size:13px;line-height:23.5px">Lorem ipsum dolor sit amet, consectetur adipiscing elit, sed do eiusmod tempor incididunt ut laborefg et dolore magna aliqua. Ut enim ad minim veniam, quis nostrud exercitation ullamco laboris nisi ut aliquip ex ea commodo consequat. Duis aute irure dolor in reprehenderit in voluptate velit esse cillum dolore eu fugiat nulla pariatur. Excepteur sint occaecat cupidatat non proident, sunt in culpa qui officia deserunt mollit anim id est laborum.</p>
  <div class="abs btn" style="left:649px;top:490px;width:156px;height:43px;background:var(--teal)">Contact us
    <svg width="18" height="14" viewBox="0 0 18 14"><path d="M1 7h15M10 1l6 6-6 6" stroke="#fff" stroke-width="2" fill="none"/></svg></div>
</section>

<section class="reviews" role="img" aria-label="Dark blue photo of a team meeting behind the testimonials">
  <div class="abs center label" style="top:65px;color:#fff">Our testimonials</div>
  <h2 class="abs center" style="top:102px;font-size:36px;color:#fff">Reviews From Clients</h2>
  <p class="abs" style="left:245px;top:181px;width:710px;text-align:center;font-size:13px;line-height:24px;color:#e4e9f1">Lorem ipsum dolor sit amet, consectetur adipiscing elit, sed do eiusmod tempor incididunt ut labore fg et dolore magna aliqua. Ut enim ad mi</p>

  <div class="abs card" style="left:94px">
    <div class="avatar" role="img" aria-label="Client portrait" style="background:linear-gradient(135deg,#e3d2c0,#9a8a7a)"></div>
    <div class="q">“</div>
    <p>Lorem ipsum dolor sit amet, con sectetur adipiscing elit, sed do eiusmod tempor incididunt</p>
    <div class="name">Elena Marsh</div>
    <div class="place"><svg width="8" height="10" viewBox="0 0 10 12"><path d="M5 11S1 7 1 4.5a4 4 0 018 0C9 7 5 11 5 11z" fill="#1a9ed8"/></svg>Los Angeles</div>
  </div>
  <div class="abs card" style="left:614px">
    <div class="avatar" role="img" aria-label="Client portrait" style="background:linear-gradient(135deg,#c9c1b6,#5b554f)"></div>
    <div class="q">“</div>
    <p>Lorem ipsum dolor sit amet, con sectetur adipiscing elit, sed do eiusmod tempor incididunt</p>
    <div class="name">Elena Marsh</div>
    <div class="place"><svg width="8" height="10" viewBox="0 0 10 12"><path d="M5 11S1 7 1 4.5a4 4 0 018 0C9 7 5 11 5 11z" fill="#1a9ed8"/></svg>Los Angeles</div>
  </div>
</section>

<section class="contact">
  <svg class="abs" style="left:0;top:0" width="1200" height="1057" viewBox="0 0 1200 1057">
    <path d="M0 500 C60 560 130 640 170 680 L170 1057 L0 1057Z" fill="#1b3554"/>
    <path d="M1038 630 C1090 610 1150 600 1200 585 L1200 1057 L1038 1057Z" fill="#1b3554"/>
    <rect x="0" y="773" width="1200" height="284" fill="#1b3554"/>
  </svg>
  <div class="abs center label" style="top:106px">Contact us</div>
  <h2 class="abs center" style="top:138px;font-size:36px;color:var(--heading)">Get in touch with us</h2>
  <p class="abs" style="left:250px;top:219px;width:700px;text-align:center;font-size:13px;line-height:24px">Lorem ipsum dolor sit amet, consectetur adipiscing elit, sed do eiusmod tempor incididunt ut labore fg et dolore magna aliqua. Ut enim ad mi</p>

  <div class="abs form-card">
    <div class="abs bar"></div>
    <h2 class="abs">Feel free to write us<br>for any type of</h2>
    <div class="abs field" style="top:138px;height:37px">Full Name</div>
    <div class="abs field" style="top:193px;height:37px">Enter Email address</div>
    <div class="abs field" style="top:245px;height:70px">Your Messages</div>
    <div class="abs submit">SUBMIT NOW</div>
    <div class="abs divider"></div>
    <div class="abs info" style="top:63px"><i><svg width="10" height="12" viewBox="0 0 10 12"><path d="M5 11S1 7 1 4.5a4 4 0 018 0C9 7 5 11 5 11z" fill="#fff"/></svg></i><span>Harrow Bay<br>Larkfield Row<br>Brookmere<br>Eastland</span></div>
    <div class="abs info" style="top:178px"><i><svg width="10" height="10" viewBox="0 0 10 10"><path d="M2 1l2 2-1 1.5c1 1.5 1.5 2 3 3L7.5 6l2 2-1.5 1.5C4 9 1 6 .5 1.5z" fill="#fff"/></svg></i><span>555 - 014 - 2298</span></div>
    <div class="abs info" style="top:234px"><i><svg width="11" height="8" viewBox="0 0 11 8"><rect x=".5" y=".5" width="10" height="7" fill="none" stroke="#fff"/><path d="M.5.5 5.5 4.5l5-4" fill="none" stroke="#fff"/></svg></i><span>hello@harrowbay-mail.net</span></div>
    <div class="abs info" style="top:285px"><i><svg width="10" height="8" viewBox="0 0 10 8"><path d="M1 0l4 4-4 4zM5 0l4 4-4 4z" fill="#fff"/></svg></i><span>8 am - 5pm&nbsp; Mon - Fri</span></div>
    <div class="abs" style="left:491px;top:352px;font-size:12px;color:var(--accent)">Reach us here:</div>
  </div>
</section>

<div class="abs footer-top"><i></i>HARROW BAY</div>
<div class="abs fsep" style="left:409px"></div>
<div class="abs fitem" style="left:432px"><svg width="26" height="26" viewBox="0 0 26 26"><circle cx="13" cy="13" r="11" fill="none" stroke="#fff" stroke-width="1.5"/><ellipse cx="13" cy="13" rx="5" ry="11" fill="none" stroke="#fff" stroke-width="1.5"/><path d="M2 13h22" stroke="#fff" stroke-width="1.5"/></svg><span>48 Larkfield Row<br>Brookmere, ST 40721</span></div>
<div class="abs fsep" style="left:668px"></div>
<div class="abs fitem" style="left:690px"><svg width="18" height="26" viewBox="0 0 18 26"><rect x="1" y="1" width="16" height="24" rx="3" fill="none" stroke="#fff" stroke-width="1.5"/><path d="M7 21h4" stroke="#fff" stroke-width="1.5"/></svg><span>PHONE<br>(555) 014 2298</span></div>
<div class="abs fsep" style="left:847px"></div>
<div class="abs fitem" style="left:865px"><svg width="28" height="22" viewBox="0 0 28 22"><rect x="1" y="1" width="26" height="20" fill="none" stroke="#fff" stroke-width="1.5"/><path d="M1 1l13 11L27 1" fill="none" stroke="#fff" stroke-width="1.5"/></svg><span>EMAIL<br>office@harrowbay-mail.net</span></div>

<nav class="abs fnav">
  <a style="left:23px">HOME</a>
  <a style="left:117px">SERVICES</a>
  <a style="left:223px">ABOUT US</a>
  <a style="left:342px">TESTIMONIALS</a>
  <a style="left:493px">BLOG</a>
  <a style="left:585px">CONTACT US</a>
</nav>

<div class="abs copy">Harrow Bay Consulting</div>
<div class="abs social" style="left:935px"></div>
<div class="abs social" style="left:966px"></div>
<div class="abs social" style="left:998px"></div>
<div class="abs social" style="left:1032px"></div>

</body>
</html>
```